TalkWell Needs a Business Card

We need a business card for Tomas Ferreby, Ph.D., CCC-SLP, who is affiliated with Hollander Ridge University. He is an Associate Professor and Licensed Speech-Language Pathologist, Department of Communication Disorders, College of Health and Human Services.

He has a consulting business "TalkWell Consultant". The logo is attached. The consulting company color is Turquoise. HRU school color is orange.

The consulting business focus on: Consultation, Research & Professional Development. Our target market is individuals with annual family income of $100,000.00 or more for consultation and speech-language pathologists for professional development activities.

No harsh colors, subtle colors appreciated. Address, e-mail, telephone, and small scan logo for a link to our website. Creativity in design will be appreciated. Please add your comments, why you created this design?

Thanks and looking for submissions.

```html
<!DOCTYPE html>
<html lang="en">
<head>
<meta charset="utf-8">
<title>TalkWell Consultants – Business Card</title>
<link rel="stylesheet" href="https://fonts.googleapis.com/css2?family=Open+Sans:wght@400;600;700&display=swap">
<style>
  :root {
    --backdrop: #b3b3b3;
    --card: #ffffff;
    --turquoise: #5bc6cf;
    --green: #5dbb4f;
    --shadow: rgba(0, 0, 0, 0.22);
  }
  * { box-sizing: border-box; margin: 0; padding: 0; }
  html, body {
    width: 1200px;
    height: 646px;
    overflow: hidden;
    background: var(--backdrop);
    font-family: "Open Sans", sans-serif;
  }
  .canvas {
    position: relative;
    width: 1200px;
    height: 646px;
  }
  .card {
    position: absolute;
    top: 175px;
    width: 520px;
    height: 297px;
    background: var(--card);
    box-shadow: 0 6px 18px var(--shadow);
    overflow: hidden;
  }
  .card--details { left: 60px; }
  .card--brand { left: 620px; }

  /* details side */
  .corner-band {
    position: absolute;
    top: 0;
    right: 0;
    width: 200px;
    height: 110px;
  }
  .corner-mark {
    position: absolute;
    top: 18px;
    right: 34px;
    width: 26px;
    height: 26px;
    background: var(--card);
  }
  .brand-lockup {
    position: absolute;
    display: flex;
    align-items: center;
  }
  .card--details .brand-lockup { left: 34px; top: 62px; gap: 14px; }
  .brand-square {
    background: var(--turquoise);
    flex: none;
  }
  .card--details .brand-square { width: 44px; height: 44px; }
  .brand-name {
    color: var(--turquoise);
    font-weight: 400;
    white-space: nowrap;
    line-height: 1;
  }
  .card--details .brand-name { font-size: 24px; }

  .rule {
    position: absolute;
    left: 34px;
    height: 2px;
    background: var(--turquoise);
  }
  .rule--upper { top: 150px; width: 452px; }
  .rule--lower { top: 232px; width: 300px; }

  .person {
    position: absolute;
    left: 34px;
    top: 196px;
    color: var(--turquoise);
    font-weight: 700;
    font-size: 22px;
    line-height: 1;
    white-space: nowrap;
  }
  .person .credentials {
    font-weight: 400;
    font-size: 12px;
    margin-left: 6px;
  }
  .contact {
    position: absolute;
    left: 34px;
    top: 246px;
    color: var(--green);
    font-weight: 600;
    font-size: 15px;
  }

  /* brand side */
  .card--brand .brand-lockup { left: 56px; top: 0; bottom: 0; gap: 24px; }
  .card--brand .brand-square { width: 86px; height: 86px; }
  .card--brand .brand-name {
    display: flex;
    flex-direction: column;
    gap: 6px;
    font-size: 40px;
  }
</style>
</head>
<body>
<main class="canvas">

  <section class="card card--details" aria-label="Card back with contact details">
    <svg class="corner-band" viewBox="0 0 200 110" aria-hidden="true">
      <polygon points="40,0 200,0 200,96" fill="var(--turquoise)" opacity="0.9"/>
      <line x1="26" y1="0" x2="200" y2="104" stroke="var(--green)" stroke-width="2"/>
    </svg>
    <span class="corner-mark"></span>

    <div class="brand-lockup">
      <span class="brand-square"></span>
      <span class="brand-name">TalkWell Consultants</span>
    </div>

    <span class="rule rule--upper"></span>
    <p class="person">Tomas Ferreby<span class="credentials">Ph.D., CCC-SLP</span></p>
    <span class="rule rule--lower"></span>
    <p class="contact">phone number, email, website</p>
  </section>

  <section class="card card--brand" aria-label="Card front with brand name">
    <div class="brand-lockup">
      <span class="brand-square"></span>
      <span class="brand-name"><span>TalkWell</span><span>Consultants</span></span>
    </div>
  </section>

</main>
</body>
</html>
```